依頼詳細
PCとスマホデザインの両方納品をいただきますが、
まずはデザインイメージが確認しやすいPCページのみの提案をお願いします。
スマホページは当選者に納品時にお願いしたいと思います。
スマホサイズは横幅750pxのサイズで作成してください。

レスポンシブウェブデザインを意識したデザインでお願いします。

デザインに関しては、添付してあるデザインレイアウト設計シートを基にお願いします。
参考サイトのURLはデザインレイアウト設計シートに記載してあります。

画像データについては、フリー素材から流用してイメージ画像に当て込んでください。

足りない場合は、一旦他のサイトの写真をサンプルとして入れてください。
また、購入が必要な写真などを利用した場合、価格とサイト名を教えてください。
ページ数
1ページ
希望イメージ
シンプル 複雑
単色 カラフル
暗い 明るい
日常 高級
遊び心 厳粛
未来的 伝統的
女性的 男性的
納品ファイル
• イラストレーター形式 (.ai)
• フォトショップ形式 (.psd)
• PNG形式 (.png)
補足説明
上記のいずれか1つ(アウトラインありとなしの2つ)と高解像度JPGを納品お願いします。

クライアント様より選定いただきました。
一番イメージに近いものでした

ご提案ありがとうございました。
また機会がありましたら是非お願いします。

```html
<!DOCTYPE html>
<html lang="ja">
<head>
<meta charset="utf-8">
<title>緑川製作所</title>
<link href="https://fonts.googleapis.com/css2?family=Noto+Sans+JP:wght@400;500;700;900&family=Russo+One&display=swap" rel="stylesheet">
<style>
:root{
  --green:#4f9a3c;
  --green-dark:#3b7f2c;
  --green-light:#8fc07c;
  --green-pale:#b9d8aa;
  --gray-bg:#efefef;
  --text:#222;
  --muted:#666;
  --line:#c9c9c9;
  --white:#fff;
}
*{margin:0;padding:0;box-sizing:border-box}
html,body{width:1200px;height:4684px;overflow:hidden;background:var(--white);color:var(--text);font-family:"Noto Sans JP",sans-serif}
.page{position:relative;width:1200px;height:4684px}
.abs{position:absolute}

/* hero */
.hero{left:0;top:0;width:1200px;height:790px;background:linear-gradient(180deg,var(--green-pale),var(--green-light))}
.hero-art{left:0;top:0;width:1200px;height:790px;background:radial-gradient(ellipse at 50% 40%,rgba(255,255,255,.25),transparent 60%),linear-gradient(180deg,#a7cd96 0%,#8fbe7c 70%,#9cc78a 100%)}
.logo{left:50px;top:36px;width:110px;height:34px;border:1px solid var(--white);color:var(--white);font-size:14px;display:flex;align-items:center;justify-content:center;letter-spacing:.1em}
.nav{right:40px;top:40px;display:flex;gap:22px;font-size:15px;color:var(--white);font-weight:500}
.hero-frame{left:330px;top:200px;width:510px;height:450px;border:10px solid var(--white);display:flex;flex-direction:column;align-items:center;justify-content:center;color:var(--white);font-weight:900;line-height:1.15}
.hero-frame .l1{font-size:96px}
.hero-frame .l2{font-size:116px;letter-spacing:.05em}
.hero-frame .l3{font-size:96px}

/* headings */
.en-title{font-family:"Russo One",sans-serif;font-size:72px;letter-spacing:.04em;line-height:1}
.en-title.outline{color:transparent;-webkit-text-stroke:2px var(--green-light)}
.en-title.solid{color:var(--green-pale)}
.title-rule{height:2px;background:var(--green-pale)}
.sub{font-size:17px;font-weight:500}
.body{font-size:14px;line-height:1.7;color:var(--text)}
.btn{background:var(--green);color:var(--white);font-size:14px;display:flex;align-items:center;justify-content:center;box-shadow:0 3px 6px rgba(0,0,0,.2)}

/* about */
.photo-racks{left:545px;top:890px;width:605px;height:260px;background:linear-gradient(135deg,#c23a2f 0%,#d9d2c8 40%,#5f88c2 75%,#c23a2f 100%)}

/* quote */
.quote-band{left:0;top:1345px;width:1200px;height:235px;background:linear-gradient(90deg,#7fb86a,var(--green-dark))}
.quote-band .q{font-family:"Russo One",sans-serif;font-size:60px;color:var(--white);line-height:1}
.quote-text{left:0;top:1442px;width:1200px;text-align:center;color:var(--white);font-size:16px}

/* product */
.product{left:0;top:1590px;width:1200px;height:560px;background:var(--gray-bg)}
.photo-product{left:50px;top:1740px;width:540px;height:390px;background:linear-gradient(180deg,#e9e9e9,#dcdcdc)}

/* news */
.news-row{left:160px;width:895px;height:92px;border-bottom:1px solid var(--line);display:flex;align-items:center;font-size:14px}
.news-row .date{width:180px;padding-left:18px}
.news-row .ttl{width:220px}

/* cards */
.card{top:2895px;width:535px;height:200px;display:flex;flex-direction:column;align-items:center;justify-content:center;color:var(--white)}
.card .en-title{font-size:58px;color:var(--white)}
.card .ja{font-size:26px;margin-top:6px;letter-spacing:.08em}
.card-recruit{left:50px;background:linear-gradient(120deg,#3c3c3c,#6e6c66)}
.card-contact{left:615px;background:linear-gradient(120deg,#4a4d55,#8d8f94)}

/* footer */
.footer{left:0;top:3210px;width:1200px;height:280px;background:linear-gradient(90deg,#6fae5a,var(--green-dark));color:var(--white)}
.tel-box{left:50px;top:3352px;width:470px;height:66px;border:2px solid var(--white);display:flex;align-items:center;gap:40px;padding-left:18px;font-size:20px}
.tel-box span{display:flex;align-items:center;gap:10px}
.tag{font-size:11px;background:var(--white);color:var(--green-dark);padding:2px 4px;font-weight:700}
</style>
</head>
<body>
<div class="page">

  <!-- hero -->
  <section class="hero abs">
    <div class="hero-art abs" role="img" aria-label="倉庫で荷物を運ぶ作業員とフォークリフトのイラスト"></div>
    <div class="logo abs">緑川製作所</div>
    <nav class="nav abs"><span>事業内容</span><span>製品情報</span><span>採用情報</span><span>会社概要</span><span>お問い合わせ</span></nav>
    <div class="hero-frame abs">
      <div class="l1">誠実を</div>
      <div class="l2">積み</div>
      <div class="l3">重ねる</div>
    </div>
  </section>

  <!-- about -->
  <div class="en-title outline abs" style="left:50px;top:880px">ABOUT US</div>
  <div class="title-rule abs" style="left:420px;top:935px;width:80px"></div>
  <div class="sub abs" style="left:50px;top:960px">緑川製作所について</div>
  <p class="body abs" style="left:50px;top:1025px;width:440px">保管と物流の現場を支えるラックを製造しています。<br>設計から製作まで一貫して対応し、安全で効率的な保管環境をご提案いたします。長年の技術を活かしお客様に寄り添います。</p>
  <div class="btn abs" style="left:50px;top:1160px;width:182px;height:44px">会社概要を見る</div>
  <div class="photo-racks abs" role="img" aria-label="倉庫に並ぶ赤い保管ラックの写真"></div>

  <!-- quote -->
  <section class="quote-band abs">
    <div class="q abs" style="left:255px;top:65px">“</div>
    <div class="q abs" style="left:905px;top:65px">”</div>
  </section>
  <p class="quote-text abs">「物流と倉庫の収納・保管」の効率化・安全化を提案します</p>

  <!-- product -->
  <section class="product abs"></section>
  <div class="photo-product abs" role="img" aria-label="赤い積み重ね式ラック製品の写真"></div>
  <div class="en-title solid abs" style="left:710px;top:1730px">STACKER</div>
  <div class="title-rule abs" style="left:1070px;top:1785px;width:80px"></div>
  <div class="sub abs" style="left:710px;top:1808px">スタッカーについて</div>
  <p class="body abs" style="left:710px;top:1850px;width:430px">積み重ねて使える保管用ラックです。<br>限られた空間を有効に活用でき、使わない時は重ねて省スペースに収納できます。耐久性にも優れています。</p>
  <div class="btn abs" style="left:710px;top:1975px;width:182px;height:44px">詳しく見る</div>

  <!-- news -->
  <div class="en-title solid abs" style="left:495px;top:2212px">NEWS</div>
  <div class="title-rule abs" style="left:700px;top:2268px;width:70px"></div>
  <div class="sub abs" style="left:0;top:2300px;width:1200px;text-align:center;font-size:16px">お知らせ</div>
  <div class="news-row abs" style="top:2330px"><span class="date">2021.03.21</span><span class="ttl">お知らせタイトル</span><span>新製品の情報を掲載しました。</span></div>
  <div class="news-row abs" style="top:2422px"><span class="date">2021.03.21</span><span class="ttl">お知らせタイトル</span><span>営業日のご案内を更新しました。</span></div>
  <div class="news-row abs" style="top:2514px"><span class="date">2021.03.21</span><span class="ttl">お知らせタイトル</span><span>採用情報を掲載しました。</span></div>
  <div class="news-row abs" style="top:2606px"><span class="date">2021.03.21</span><span class="ttl">お知らせタイトル</span><span>ホームページを公開しました。</span></div>
  <div class="btn abs" style="left:510px;top:2762px;width:182px;height:44px">詳しく見る</div>

  <!-- cards -->
  <a class="card card-recruit abs" role="img" aria-label="オフィスで働く人の手元の写真"><span class="en-title">RECRUIT</span><span class="ja">採用情報はこちら</span></a>
  <a class="card card-contact abs" role="img" aria-label="ノートパソコンを操作する手元の写真"><span class="en-title">CONTACT</span><span class="ja">お問い合わせはこちら</span></a>

  <!-- footer -->
  <footer class="footer abs">
    <div class="abs" style="left:50px;top:36px;font-size:14px;letter-spacing:.1em">緑川製作所</div>
    <nav class="abs" style="right:50px;top:58px;display:flex;gap:22px;font-size:14px"><span>事業内容</span><span>製品情報</span><span>採用情報</span><span>会社概要</span><span>お問い合わせ</span></nav>
    <div class="abs" style="left:50px;top:100px;font-size:13px">〒000-0000　新潟県緑川市本町1-2-3</div>
    <div class="abs" style="left:50px;top:222px;font-size:13px;display:flex;gap:24px"><span>個人情報保護方針</span><span>サイトポリシー</span></div>
    <div class="abs" style="right:50px;top:178px;font-size:12px">© Copyright 緑川製作所</div>
  </footer>
  <div class="tel-box abs" style="color:var(--white)">
    <span><em class="tag">TEL</em>000-12-3456</span>
    <span><em class="tag">FAX</em>000-12-3457</span>
  </div>

</div>
</body>
</html>
```